brightwave - Property Management DL Card

I am after a savvy designer to cut through junk mail! so many real estate agents use flyers to promote themselves and their business and usually sales. We are a property management firm (residential) and we want to represent landlords that have existing investment properties and need a quality agent to represent them. Can you help?
DL size, will be printed and delivered to mailboxes. For a look at our website go to www.brightwavehq.com.au. Keep it simple and clutter free.
it is to be double sided - with one side to be simple and clear - just our website, logo and telephone number on the back.
attached is our logo and our telephone number is 1300 42 18 96
the above are 2 essential elements to be included + our email address: admin@brightwavehq.com.au
also attached are our transparent price list

Target Market(s)
property investors,
people that manage properties themselves
Industry/Entity Type
Property Management
Other font styles liked:
- arial
Look and feel

```html
<!DOCTYPE html>
<html lang="en">
<head>
<meta charset="utf-8">
<title>brightwave – Property Management DL Card</title>
<link href="https://fonts.googleapis.com/css2?family=Mulish:wght@300;400;500&family=Open+Sans:ital,wght@1,400&display=swap" rel="stylesheet">
<style>
  :root {
    --stage: #000000;
    --white: #ffffff;
    --ink: #1a1a1a;
    --grey-text: #4d4d4f;
    --card-grey: #e6e7e8;
    --brand-red: #e3161f;
    --icon-grey: #58595b;
    --caption: #c8c8c8;
  }
  * { margin: 0; padding: 0; box-sizing: border-box; }
  html, body {
    width: 1149px; height: 1200px; overflow: hidden;
    background: var(--stage);
    font-family: "Mulish", Arial, sans-serif;
  }
  .canvas { position: relative; width: 1149px; height: 1200px; }
  .side-label {
    position: absolute; top: 66px;
    color: var(--white); font-size: 31px; font-weight: 400;
  }
  .side-label--front { left: 107px; }
  .side-label--back { left: 585px; }

  .card { position: absolute; top: 117px; width: 460px; height: 965px; overflow: hidden; }
  .card--front { left: 105px; }
  .card--back { left: 584px; background: var(--card-grey); }

  /* Front */
  .city-photo {
    position: absolute; inset: 0;
    background: linear-gradient(180deg,
      #cfe6f3 0%, #b5d5ea 10%, #9fb8c4 20%, #8a7f6c 30%,
      #4c9ab0 40%, #3f8fa6 46%, #6f6a4a 55%, #7a5f3a 68%,
      #4f5a35 80%, #5c5a44 100%);
  }
  .tagline {
    position: absolute; top: 36px; left: 0; width: 460px;
    text-align: center; font-size: 23px; font-weight: 500; color: var(--ink);
  }
  .logo-block {
    position: absolute; top: 116px; left: 0; width: 287px; height: 175px;
    background: var(--stage);
    display: flex; flex-direction: column; align-items: center; justify-content: center;
    color: var(--white); font-weight: 300;
  }
  .logo-block .brand-name { font-size: 50px; line-height: 1; letter-spacing: -0.5px; }
  .logo-block .brand-sub { font-size: 25px; line-height: 1.2; }
  .benefits { position: absolute; inset: 0; }
  .benefit-text {
    font-family: "Mulish", Arial, sans-serif; font-size: 19px; font-weight: 500;
    fill: var(--white); text-anchor: middle;
  }

  /* Back */
  .lift-photo {
    position: absolute; top: 0; left: 0; width: 460px; height: 307px;
    background: linear-gradient(135deg, #2a2a2a 0%, #6a6763 45%, #4a4845 70%, #1e1e1e 100%);
  }
  .definition-band {
    position: absolute; top: 307px; left: 0; width: 460px; height: 45px;
    background: var(--stage);
    display: flex; align-items: center; justify-content: center;
    font-family: "Open Sans", Arial, sans-serif; font-style: italic;
    font-size: 15px; color: var(--caption);
  }
  .interior-photo {
    position: absolute; top: 352px; left: 0; width: 460px; height: 257px;
    background: linear-gradient(180deg, #6e6a78 0%, #b9a08a 40%, #8f7b68 70%, #3c342e 100%);
  }
  .contact {
    position: absolute; top: 609px; left: 0; width: 460px; height: 356px;
    color: var(--grey-text);
  }
  .contact .brand-name {
    position: absolute; top: 80px; width: 100%; text-align: center;
    font-size: 41px; font-weight: 300; color: var(--ink); line-height: 1;
  }
  .contact .brand-sub {
    position: absolute; top: 120px; width: 100%; text-align: center;
    font-size: 20px; font-weight: 300; color: var(--ink);
  }
  .contact .address {
    position: absolute; top: 161px; width: 100%; text-align: center; font-size: 16px;
  }
  .contact .line-item {
    position: absolute; width: 100%; text-align: center; font-size: 16px;
  }
  .contact .line-item--phone { top: 225px; }
  .contact .line-item--email { top: 285px; }
  .contact-icons { position: absolute; inset: 0; }
</style>
</head>
<body>
<div class="canvas">
  <div class="side-label side-label--front">Front</div>
  <div class="side-label side-label--back">Back</div>

  <section class="card card--front">
    <div class="city-photo" role="img" aria-label="Aerial photo of a harbour city skyline with bridge, water and leafy suburbs at sunset"></div>
    <p class="tagline">Property Management Specialists</p>
    <div class="logo-block">
      <span class="brand-name">brightwave</span>
      <span class="brand-sub">property group</span>
    </div>
    <svg class="benefits" width="460" height="965" viewBox="0 0 460 965">
      <path d="M460 417 C 380 425, 310 450, 290 500 C 250 560, 220 610, 240 680 C 260 760, 300 830, 360 860 C 400 880, 430 885, 460 885"
            fill="none" stroke="#ffffff" stroke-width="4"/>
      <g stroke="#ffffff" stroke-width="3" fill="#e3161f">
        <ellipse cx="307" cy="481" rx="81" ry="46"/>
        <ellipse cx="243" cy="605" rx="81" ry="46"/>
        <ellipse cx="266" cy="727" rx="81" ry="46"/>
        <ellipse cx="337" cy="855" rx="81" ry="46"/>
      </g>
      <text class="benefit-text" x="307" y="478">No Postage &amp;</text>
      <text class="benefit-text" x="307" y="501">Admin Fees</text>
      <text class="benefit-text" x="243" y="602">No Hidden</text>
      <text class="benefit-text" x="243" y="625">Extras</text>
      <text class="benefit-text" x="266" y="721">Excellent</text>
      <text class="benefit-text" x="266" y="744">Communication</text>
      <text class="benefit-text" x="337" y="850">Technology</text>
      <text class="benefit-text" x="337" y="873">Focussed</text>
    </svg>
  </section>

  <section class="card card--back">
    <div class="lift-photo" role="img" aria-label="Close-up photo of a brushed metal lift panel with glowing up display and call buttons"></div>
    <div class="definition-band">brightwave definition - “raise or lift to a higher position”</div>
    <div class="interior-photo" role="img" aria-label="Photo of a modern apartment living room with sofa, armchairs, dining area and city-view windows at dusk"></div>
    <div class="contact">
      <span class="brand-name">brightwave</span>
      <span class="brand-sub">property group</span>
      <p class="address">PO Box B527 Harbourside NSW 2099</p>
      <svg class="contact-icons" width="460" height="356" viewBox="0 0 460 356">
        <g fill="none" stroke="#58595b" stroke-width="1.5">
          <path d="M128 222 Q 230 190 332 222"/>
          <path d="M128 282 Q 230 250 332 282"/>
        </g>
        <circle cx="230" cy="206" r="14" fill="#58595b"/>
        <path d="M226 199 q -4 7 0 14 l 3 -1 -1 -3 q -2 -3 0 -6 l 1 -3 z" fill="#ffffff"/>
        <circle cx="230" cy="266" r="14" fill="#58595b"/>
        <g fill="none" stroke="#ffffff" stroke-width="1.4">
          <rect x="223" y="261" width="14" height="10"/>
          <path d="M223 261 l 7 6 7 -6"/>
        </g>
      </svg>
      <p class="line-item line-item--phone">1300 42 18 96</p>
      <p class="line-item line-item--email">admin@brightwavehq.com.au</p>
    </div>
  </section>
</div>
</body>
</html>
```